Gavin Holloway Advisory - Web Design Project

We need a web design for my new edgy consulting business specializing in innovation, technology and strategy.

It is our personal goal to turn each client into raving fans by helping them achieve their own business goals and aspirations through assisting them in raising their own innovation and marketing standards.

We provide our personalised and state-of-the-art services to our clients and boards who represent some of the world greatest innovative thinkers.

Here is some other information which may help shape your thinking.

I've had direct Involvement in the development of the following iPad, iPhone Applications and websites

PelicanTrailsHub.com (TerraLoom platform) by Coastline Visitor Bureau
http://pelicantrailshub.example

Harbor Zest by Tidy Sailways
https://apps.example.net/au/app/harbor-zest/id900111222

RedDustGo by Frontier Visits Office
https://apps.example.net/au/app/reddustgo/id900111333

Wexbridge Rambles
http://www.wexbridgerambles.example

Trip Weaver by Coastline Visitor Bureau
http://apps.example.net/au/app/trip-weaver/id900111444

Sunward by Sunward Travel Board
https://apps.example.net/au/app/sunward/id900111555

Fernvale Ridge Road Loop by Roamwell Agency
https://apps.example.net/au/app/fernvale-ridge-road-loop/id900111666

Pathfinder Run by Frontier Visits Office and Southern Coast Visitor Council
https://apps.example.net/au/app/pathfinder-run-grand-trek/id900111777

Gavin Holloway Advisory (GHA)
November 2012 – Present (8 months)Brisbane, Sydney, Canberra

Gavin’s consults to Small-to-Medium Enterprises (SME) and Government organisations on business strategy, technology strategy, risk mitigation, disruptive technology and innovation in the workplace.

Gavin’s consultancy mantra is that we cannot divorce economic life from cultural life particularly in an era when social capital may be as important as physical capital in business.

Reason: request from designers, I want to see their best efforts

Target Market(s)

35+

Industry/Entity Type

Business

Requirements
Must have
• Please use some of the personal image(s) contained in the zip files which can be downloaded from here

http://filedrop.example/k7Pq2Lm9
http://filedrop.example/r4Tz8Hv1
http://filedrop.example/w6Nc3Bx5
Nice to have
• Black, Sleek design, maybe minimalist. Nice to have a Glint for the design. Nice to have it easily ported to Wordpress or be a modified Wordpress template. HTML 5, responsive design

```html
<!DOCTYPE html>
<html lang="en">
<head>
<meta charset="utf-8">
<title>Gavin Holloway Advisory</title>
<link href="https://fonts.googleapis.com/css2?family=Open+Sans:wght@300;400&family=Arimo:wght@400;700&display=swap" rel="stylesheet">
<style>
  :root {
    --page: #ffffff;
    --band-top: #050505;
    --band-bottom: #2a2a2a;
    --ink: #111111;
    --body: #2b2b2b;
    --muted: #6f6f6f;
    --button: #0d4a7e;
    --white: #ffffff;
    --footer-text: #cfcfcf;
    --bubble-line: #dcdcdc;
    --tile-navy: #14203d;
    --tile-blue: #2f57b8;
    --tile-slate: #3c4a57;
    --tile-peach: #fbd2be;
    --tile-sky: #5aa6df;
    --tile-dark: #2e2e2e;
  }
  * { margin: 0; padding: 0; box-sizing: border-box; }
  html, body { width: 688px; height: 1200px; overflow: hidden; background: var(--page); }
  body { position: relative; font-family: "Open Sans", sans-serif; }

  .column { position: absolute; left: 208px; top: 11px; width: 265px; height: 1189px; background: var(--page); }

  .intro {
    position: absolute; left: 0; top: 0; width: 265px; height: 180px;
    background: linear-gradient(to bottom, var(--band-top) 55%, var(--band-bottom));
    color: var(--white); text-align: center;
    font-size: 14.5px; line-height: 21px; padding: 12px 8px 0;
  }

  .section-title { position: absolute; color: var(--ink); font-weight: 400; white-space: nowrap; }
  .clients-title { left: 0; width: 265px; text-align: center; top: 216px; font-size: 21px; }
  .clients-title .light { font-weight: 300; }

  .client-tile {
    position: absolute; width: 80px; height: 71px;
    display: flex; align-items: center; justify-content: center; text-align: center;
    font-size: 11px; line-height: 14px; color: var(--white); padding: 4px;
    border: 1px solid #1a1a1a;
  }
  .tile-pelican { left: 41px; top: 268px; background: var(--tile-navy); }
  .tile-harbor  { left: 135px; top: 268px; background: var(--tile-blue); }
  .tile-reddust { left: 41px; top: 352px; background: var(--tile-slate); }
  .tile-wexbridge { left: 135px; top: 352px; background: var(--tile-peach); color: #4a2b18; border-color: #6b4a34; }
  .tile-sunward { left: 41px; top: 437px; background: var(--tile-sky); }
  .tile-more { left: 135px; top: 437px; background: var(--tile-dark); font-size: 17px; line-height: 21px; }

  .news-title { left: 29px; top: 546px; font-size: 27px; }
  .copy { position: absolute; left: 28px; width: 215px; font-family: "Arimo", sans-serif; font-size: 10.5px; line-height: 17px; color: var(--body); }
  .news-lead { top: 594px; }
  .news-sub { top: 658px; color: var(--muted); }

  .button {
    position: absolute; left: 27px; width: 74px; height: 22px;
    background: var(--button); color: var(--white); border-radius: 3px;
    font-size: 12px; line-height: 22px; text-align: center;
  }
  .news-button { top: 704px; }

  .testimonials-title { left: 27px; top: 754px; font-size: 27px; }
  .bubble { position: absolute; left: 14px; top: 797px; width: 238px; height: 124px; }
  .quote { position: absolute; left: 32px; top: 810px; width: 210px; font-family: "Arimo", sans-serif; font-size: 10.5px; line-height: 18px; color: var(--body); }
  .quote-author { position: absolute; left: 32px; top: 873px; font-family: "Arimo", sans-serif; font-weight: 700; font-size: 10.5px; color: #8a8a8a; }
  .testimonial-button { top: 914px; }

  .site-footer {
    position: absolute; left: 0; top: 964px; width: 265px; height: 225px;
    background: linear-gradient(to bottom, var(--band-top) 60%, var(--band-bottom));
    color: var(--footer-text); text-align: center; font-family: "Arimo", sans-serif; font-size: 10px;
  }
  .footer-nav { position: absolute; left: 20px; top: 17px; width: 225px; line-height: 18px; }
  .footer-nav span { margin: 0 4px; }
  .copyright { position: absolute; left: 0; width: 265px; top: 70px; line-height: 20px; color: var(--white); }
  .social { position: absolute; left: 90px; top: 115px; }
  .wordmark { position: absolute; left: 36px; top: 155px; width: 196px; color: var(--white); font-family: "Open Sans", sans-serif; font-weight: 300; text-align: right; }
  .wordmark .name { display: block; font-size: 24px; line-height: 26px; text-align: left; white-space: nowrap; }
  .wordmark .tag { display: block; font-size: 15px; line-height: 18px; }
</style>
</head>
<body>
  <main class="column">
    <header class="intro">
      <p>Gavin’s consults to Small-to-Medium Enterprises (SME) and Government organisations on business strategy, technology strategy, risk mitigation, disruptive technology and innovation in the workplace.</p>
    </header>

    <h2 class="section-title clients-title"><span class="light">OUR</span> VALUED CLIENTS</h2>
    <div class="client-tile tile-pelican">PelicanTrailsHub</div>
    <div class="client-tile tile-harbor">Harbor Zest</div>
    <div class="client-tile tile-reddust">RedDustGo</div>
    <div class="client-tile tile-wexbridge">Wexbridge Rambles</div>
    <div class="client-tile tile-sunward">Sunward</div>
    <div class="client-tile tile-more">More Clients</div>

    <h2 class="section-title news-title">NEWS / EVENT</h2>
    <p class="copy news-lead">Lorem ipsum dolor sit amet, consectetuer adipiscing elit, sed diam nonummy nibh euismod tincidunt ut laoreet dolore magna.</p>
    <p class="copy news-sub">Consectetuer adipiscing elit, sed diam nonummy nibh euismod tincidunt ut.</p>
    <a class="button news-button">View All</a>

    <h2 class="section-title testimonials-title">TESTIMONIALS</h2>
    <svg class="bubble" viewBox="0 0 238 124" aria-hidden="true">
      <path d="M6 2 H228 Q234 2 234 8 V100 Q234 106 228 106 H166 L166 118 L150 106 H10 Q4 106 4 100 V8 Q4 2 10 2 Z" fill="#ffffff" stroke="#dcdcdc" stroke-width="2"/>
    </svg>
    <p class="quote">"Lorem ipsum dolor sit amet, consectetuer adipiscing elit, sed diam nonummy nibh euismod tincidunt ut laoreet dolore magna."</p>
    <p class="quote-author">— Daniel Brooks</p>
    <a class="button testimonial-button">View All</a>

    <footer class="site-footer">
      <nav class="footer-nav">GHA <span>|</span> Recruitment <span>|</span> Press <span>|</span> Imprint <span>|</span><br>Contact Us</nav>
      <p class="copyright">© 2013 Gavin Holloway Advisory<br>All Rights Reserved.</p>
      <svg class="social" width="90" height="26" viewBox="0 0 90 26" aria-hidden="true">
        <g fill="#3a3a3a" stroke="#bdbdbd" stroke-width="1.5">
          <rect x="5" y="5" width="16" height="16" transform="rotate(45 13 13)"/>
          <rect x="37" y="5" width="16" height="16" transform="rotate(45 45 13)"/>
          <rect x="69" y="5" width="16" height="16" transform="rotate(45 77 13)"/>
        </g>
      </svg>
      <div class="wordmark"><span class="name">Gavin Holloway</span><span class="tag">Advisory</span></div>
    </footer>
  </main>
</body>
</html>
```